Anzeigengestaltung für ein ein Messemontage Unternehmen
Zielgruppe
Wir sind ein Messemontage Unternehmen. Wir arbeiten Europa weit und suchen einen Monteur für Messestände in ganz Europa.
Gesucht wird ein cooles und lustiges Design einer Stellenanzeige.
Aufgabenstellung
Die Anzeige sollte für Quivlo und einer Internetseite kompatibel sein.
Ich bin leider nicht geübt in solchen Sachen. Deshalb einfach Fragen stellen die ich dann sehr gerne beantworte.
Hier ein paar Eckdaten die aber nicht unbedingt benutzt werden müssen.
• Messemontagen europaweit
• Teamarbeit
•eigenverantwortlich Arbeiten
• Firmenfahrzeug wird gestellt
• gute Bezahlung

```html
<!DOCTYPE html>
<html lang="de">
<head>
<meta charset="utf-8">
<title>Stellenanzeige – KORVAN Messemontagen</title>
<link rel="stylesheet" href="https://fonts.googleapis.com/css2?family=Source+Sans+3:wght@400;600;700&family=Kaushan+Script&display=swap">
<style>
  :root {
    --brand-red: #ec1c24;
    --ink: #111111;
    --text-grey: #3a3a3a;
    --white: #ffffff;
    --sky-top: #7d96b3;
    --sky-mid: #b9c6d4;
    --snow: #eef0f2;
    --ground: #e6e6e6;
  }
  * { margin: 0; padding: 0; box-sizing: border-box; }
  html, body { width: 982px; height: 1200px; overflow: hidden; background: var(--white); }
  .ad {
    position: relative;
    width: 982px;
    height: 1200px;
    overflow: hidden;
    font-family: "Source Sans 3", "Source Sans Pro", sans-serif;
  }
  .hero-photo {
    position: absolute; left: 0; top: 0; width: 982px; height: 990px;
    background:
      radial-gradient(ellipse 420px 520px at 500px 560px, rgba(255,255,255,0.85), rgba(255,255,255,0) 70%),
      linear-gradient(180deg, var(--sky-top) 0%, var(--sky-mid) 28%, #d7dde3 48%, var(--snow) 70%, var(--ground) 100%);
  }
  .headline {
    font-family: "Kaushan Script", cursive;
    color: var(--white);
    font-weight: 400;
    line-height: 1;
  }
  .headline span { position: absolute; left: 0; width: 982px; text-align: center; display: block; }
  .headline .line-one { top: 48px; font-size: 110px; }
  .headline .line-two { top: 190px; font-size: 108px; }

  .job { position: absolute; left: 44px; top: 660px; width: 380px; }
  .job-intro { font-size: 24px; font-weight: 700; color: var(--ink); line-height: 1; }
  .job-title { font-size: 31px; font-weight: 700; color: var(--brand-red); margin-top: 10px; line-height: 1; }
  .job-text { font-size: 17.5px; color: var(--text-grey); line-height: 25.5px; margin-top: 18px; }
  .benefits { font-size: 17.5px; color: var(--text-grey); line-height: 25.5px; margin-top: 20px; }
  .benefits strong { color: var(--brand-red); font-size: 22px; font-weight: 700; }
  .cta { position: absolute; left: 44px; top: 910px; font-size: 46px; font-weight: 700; color: var(--brand-red); line-height: 1; letter-spacing: 0.3px; }

  .about { position: absolute; left: 654px; top: 694px; width: 310px; }
  .about-title { font-size: 34px; font-weight: 700; color: var(--brand-red); line-height: 1; }
  .about-text { font-size: 17.5px; color: var(--text-grey); line-height: 25.5px; margin-top: 18px; }

  .footer-band { position: absolute; left: 0; top: 982px; width: 982px; height: 218px; background: var(--brand-red); }
  .footer-rule { position: absolute; left: 0; top: 1066px; width: 982px; height: 2px; background: var(--white); }
  .apply { position: absolute; left: 44px; top: 996px; font-size: 19px; font-weight: 600; color: var(--white); line-height: 26px; }

  .contact { position: absolute; color: var(--white); font-size: 18px; line-height: 29px; }
  .contact-company { left: 44px; top: 1082px; font-weight: 700; }
  .contact-address { left: 44px; top: 1111px; }
  .contact-phone { left: 354px; top: 1111px; }
  .contact-web { left: 663px; top: 1140px; }

  .brand { position: absolute; left: 720px; top: 1004px; display: flex; align-items: center; gap: 12px; }
  .brand-mark { width: 22px; height: 22px; background: var(--white); }
  .brand-name { color: var(--white); font-size: 40px; font-weight: 700; line-height: 1; }
</style>
</head>
<body>
<div class="ad">
  <div class="hero-photo" role="img" aria-label="Fotografie: verschneiter Berggipfel unter bewölktem Himmel, davor ein Wanderer mit orangefarbenem Rucksack von hinten"></div>

  <h1 class="headline">
    <span class="line-one">Sie Suchen die</span>
    <span class="line-two">Herausforderung?</span>
  </h1>

  <section class="job">
    <p class="job-intro">Wir suchen eine</p>
    <h2 class="job-title">Mitarbeiter (w/m/d)</h2>
    <p class="job-text">Wir suchen einen professionellen Mitarbeit-<br>er, der sowohl einzeln als auch im Team<br>arbeiten kann.</p>
    <p class="benefits"><strong>BENEFITS :</strong> Gute Bezahlung, Bonus,<br>Arbeitsgarantie bis zu 40 Stunden</p>
  </section>

  <p class="cta">INTERESSIERT?</p>

  <section class="about">
    <h2 class="about-title">Uber uns?</h2>
    <p class="about-text">Wir sind ein Messemontage<br>Unternehmen. Wir arbeiten Europa<br>weit und suchen einen Monteur für<br>Messestände in ganz Europa.</p>
  </section>

  <div class="footer-band"></div>
  <div class="footer-rule"></div>

  <p class="apply">Bewerben Sie Sich Jetzt per Post Oder per Email-an<br>Info@Korvan-Messemontagen.example</p>

  <p class="contact contact-company">KORVAN Messemontagen</p>
  <p class="contact contact-address">Lindenweg 12<br>12345 Talhausen</p>
  <p class="contact contact-phone">Tel. :01234/567890<br>Mobil : 0170 00 11 22 3</p>
  <p class="contact contact-web">www.korvan-messemontagen.example</p>

  <div class="brand">
    <span class="brand-mark" aria-hidden="true"></span>
    <span class="brand-name">KORVAN</span>
  </div>
</div>
</body>
</html>
```